Nirel Solutions Business Card
Stationary as well/logo for resumes, etc.
We are getting there. I need two samples...I like the black face Quorvix has going. I want the website across the bottom. I potentially want to see a black fade into a white bottom (background).
I also don't want it too busy so one color (blue) font. quorvix is close to what I am seeking
Gang,
I uploaded the files of my logo and am sorry for doing this late. What I am looking for is a business card and staionary that incorporates this. Peltcraft you are close to what I am lookign for witht he staionary- the card layout, I like tobrenik's better. In my logo there is a two tone as well, some with a black background and some with white- i want to try and explore this...

```html
<!DOCTYPE html>
<html lang="en">
<head>
<meta charset="utf-8">
<title>Nirel Solutions Stationery</title>
<link href="https://fonts.googleapis.com/css2?family=Arimo:wght@400;700&display=swap" rel="stylesheet">
<style>
  :root {
    --stage: #232323;
    --paper: #ffffff;
    --ink-dark: #2b2b2d;
    --ink-darker: #1c1c1e;
    --blue: #3aa9d6;
    --blue-light: #8ed5ee;
    --blue-deep: #1f6f95;
    --white: #ffffff;
    --grey-text: #c9c9c9;
  }
  * { box-sizing: border-box; margin: 0; padding: 0; }
  html, body { width: 1200px; height: 910px; overflow: hidden; }
  body {
    background: var(--stage);
    font-family: "Arimo", Arial, sans-serif;
    position: relative;
  }
  .brand { display: flex; align-items: center; gap: 10px; }
  .brand-dot { border-radius: 50%; background: var(--blue); flex: none; }
  .brand-name { color: var(--blue); font-weight: 700; letter-spacing: 0.04em; line-height: 1.05; white-space: nowrap; }

  /* Letterhead */
  .letterhead {
    position: absolute; left: 226px; top: 30px; width: 738px; height: 843px;
    background: var(--paper);
  }
  .letterhead .brand { position: absolute; left: 22px; top: 24px; }
  .letterhead .brand-dot { width: 70px; height: 70px; }
  .letterhead .brand-name { font-size: 30px; }
  .letterhead-contact {
    position: absolute; right: 40px; top: 14px; text-align: right;
    color: var(--blue); font-size: 15px; line-height: 1.28;
  }
  .letterhead-contact table { margin-left: auto; border-collapse: collapse; }
  .letterhead-contact td { padding: 0; text-align: left; }
  .letterhead-contact td.label { padding-right: 8px; }
  .letterhead-contact .line-gap { margin-top: 8px; }

  /* Business card front */
  .card-front {
    position: absolute; left: 369px; top: 239px; width: 271px; height: 150px;
    background: linear-gradient(180deg, #333336 0%, var(--ink-darker) 100%);
    overflow: hidden;
  }
  .card-front .person { position: absolute; left: 10px; top: 9px; color: var(--white); }
  .card-front .person-name { font-size: 11px; font-weight: 700; }
  .card-front .person-title { font-size: 7px; color: var(--grey-text); margin-top: 2px; }
  .card-front .address { position: absolute; left: 10px; top: 40px; font-size: 7px; color: var(--grey-text); line-height: 1.3; }
  .card-front .contact { position: absolute; left: 10px; top: 76px; font-size: 7px; color: var(--grey-text); line-height: 1.3; }
  .card-front .contact span { display: inline-block; width: 26px; }
  .card-front .brand { position: absolute; right: 14px; top: 42px; gap: 6px; }
  .card-front .brand-dot { width: 30px; height: 30px; }
  .card-front .brand-name { font-size: 14px; }
  .card-front .web-band {
    position: absolute; left: 0; bottom: 0; width: 100%; height: 18px;
    background: linear-gradient(90deg, var(--blue-deep), var(--blue) 60%, var(--blue-light));
    color: var(--white); font-size: 8px; font-weight: 700; line-height: 18px; padding-left: 140px;
  }

  /* Business card back */
  .card-back {
    position: absolute; left: 659px; top: 327px; width: 259px; height: 153px;
    background: linear-gradient(135deg, #3a3a3d 0%, var(--ink-dark) 55%, var(--ink-darker) 100%);
  }
  .card-back .tagline {
    position: absolute; left: 18px; top: 34px; color: var(--white);
    font-size: 18px; font-weight: 700; line-height: 1.15; width: 100px;
  }
  .card-back .brand {
    position: absolute; right: 16px; top: 26px;
    flex-direction: column; align-items: center; gap: 8px;
  }
  .card-back .brand-dot { width: 56px; height: 56px; }
  .card-back .brand-name { font-size: 12px; text-align: center; }

  /* Envelope */
  .envelope {
    position: absolute; left: 312px; top: 522px; width: 648px; height: 310px;
    background: linear-gradient(180deg, #38383b 0%, var(--ink-dark) 60%, #262628 100%);
    overflow: hidden;
  }
  .envelope .brand { position: absolute; left: 22px; top: 26px; }
  .envelope .brand-dot { width: 60px; height: 60px; }
  .envelope .brand-name { font-size: 26px; }
  .envelope .address {
    position: absolute; right: 20px; top: 14px; width: 200px; color: var(--white);
    font-size: 17px; line-height: 1.22; white-space: nowrap;
  }
  .envelope .web-band {
    position: absolute; left: 0; bottom: 16px; width: 100%; height: 44px;
    background: linear-gradient(90deg, var(--blue-deep) 0%, var(--blue) 50%, var(--blue-light) 100%);
    color: var(--white); font-size: 23px; font-weight: 700; letter-spacing: 0.03em;
    text-align: center; line-height: 44px;
  }
</style>
</head>
<body>

<section class="letterhead" aria-label="Letterhead">
  <div class="brand">
    <div class="brand-dot"></div>
    <div class="brand-name">NIREL<br>SOLUTIONS</div>
  </div>
  <div class="letterhead-contact">
    <table>
      <tr><td class="label">Phone</td><td>: 555.210.4471</td></tr>
      <tr><td class="label">Cell</td><td>: 555.210.4472</td></tr>
      <tr><td class="label">Fax</td><td>: 555.210.4473</td></tr>
    </table>
    <div class="line-gap">E-mail : kelso@nirel-it.com</div>
    <div>www.nirel-it.com</div>
  </div>
</section>

<section class="card-front" aria-label="Business card front">
  <div class="person">
    <div class="person-name">Kelso Marrin</div>
    <div class="person-title">Client Relations Director</div>
  </div>
  <div class="address">1180 Harbor Crest Drive<br>Suite 200<br>Calder, TX 77000</div>
  <div class="contact">
    <div><span>Phone</span>: 555.210.4471</div>
    <div><span>Cell</span>: 555.210.4472</div>
    <div><span>Fax</span>: 555.210.4473</div>
    <div><span>E-mail</span>: kelso@nirel-it.com</div>
  </div>
  <div class="brand">
    <div class="brand-dot"></div>
    <div class="brand-name">NIREL<br>SOLUTIONS</div>
  </div>
  <div class="web-band">www.nirel-it.com</div>
</section>

<section class="card-back" aria-label="Business card back">
  <div class="tagline">Saving<br>Your<br>Business</div>
  <div class="brand">
    <div class="brand-dot"></div>
    <div class="brand-name">NIREL<br>SOLUTIONS</div>
  </div>
</section>

<section class="envelope" aria-label="Envelope">
  <div class="brand">
    <div class="brand-dot"></div>
    <div class="brand-name">NIREL<br>SOLUTIONS</div>
  </div>
  <div class="address">1180 Harbor Crest Drive<br>Suite 200<br>Calder, TX 77000</div>
  <div class="web-band">www.nirel-it.com</div>
</section>

</body>
</html>
```